ReDesign Website for a more Bold approach

Hello! I'd like to redesign my website: holvencrest.com

I'd like to add one thing that's not on my website which is a blog. The design around the blog should be put time into as I will be putting out incredibly great content and want it to attract viewers.

I get a lot of inspiration from ruvtal.com (the way they flow the big statements across each screen, colors)
moorlane.vc (the simplicity behind the design is beautiful)

I like modern very simple but bold approaches.

I am going to attach my logo here and if it can be thought of when making the design of the website. Thanks!

Industry/Entity Type

Finance and Private Equity

Number of Pages Required

3 page

Font styles to use
Serif
Sans Serif

Colors
0054AA
0677BA
7BADD7
CADEEF
E8F1F8
0094D4
00A9DD
6FCCEA
C7EBF8
E9F6FB
00AB8E
00BBA5
67D7C9
C6EFE9
E9F9F6

Requirements
Must have
• My project must have a Home, Expertise, Story, Clients, Approach, Blog, Contact
Nice to have
• It would be nice to have these tabs reduced to 1-3 pages
Should not have
• My project must not have bright colors.

```html
<!DOCTYPE html>
<html lang="en">
<head>
<meta charset="utf-8">
<title>Holvencrest Ventures</title>
<link href="https://fonts.googleapis.com/css2?family=Playfair+Display:wght@400&family=Mulish:wght@400;700;800&display=swap" rel="stylesheet">
<style>
:root{
  --navy:#10294a;
  --hero-a:#0a6fb8;
  --hero-b:#1b83c4;
  --teal:#00bba5;
  --teal-soft:#33bba6;
  --mist:#e9f6fb;
  --blue:#0677ba;
  --blue-deep:#0054aa;
  --sky:#0094d4;
  --aqua:#6fcce9;
  --photo:#8db6db;
  --news-sub:#7badd7;
  --build:#2f78bf;
  --build-title:#9cc6ee;
  --ink:#3b3b3b;
  --grey:#9aa7b2;
  --white:#ffffff;
  --serif:'Playfair Display', serif;
  --sans:'Mulish', sans-serif;
}
*{margin:0;padding:0;box-sizing:border-box}
html,body{width:1200px;height:3900px;overflow:hidden}
body{font-family:var(--sans);color:var(--ink);background:var(--white);position:relative}
section,header{position:absolute;left:0;width:1200px}

.site-header{top:0;height:68px;background:var(--navy)}
.brand{position:absolute;left:88px;top:22px;font-family:var(--sans);font-weight:400;font-size:19px;color:var(--white)}
.nav a{position:absolute;top:26px;font-size:13px;color:var(--white);text-decoration:none}

.hero{top:68px;height:474px}
.hero-photo{position:absolute;inset:0;background:linear-gradient(180deg,var(--hero-b) 0%,var(--hero-a) 55%,#2f6fa6 100%)}
.hero-kicker{position:absolute;top:150px;width:100%;text-align:center;font-size:21px;color:var(--aqua)}
.hero-title{position:absolute;top:183px;width:100%;text-align:center;font-family:var(--serif);font-weight:400;font-size:44px;line-height:52px;color:var(--white);text-shadow:0 2px 4px rgba(0,0,0,.3)}
.hero-arrow{position:absolute;left:585px;top:400px}

.stats{top:542px;height:352px;background:var(--teal)}
.stat{position:absolute;top:185px;width:260px;text-align:center;color:var(--white)}
.stat-value{font-weight:800;font-size:40px;line-height:44px}
.stat-label{font-weight:800;font-size:17px;letter-spacing:.3px}

.expertise{top:894px;height:525px}
.expertise-panel{position:absolute;left:0;top:0;width:496px;height:525px;background:var(--mist)}
.section-title{font-family:var(--serif);font-weight:400;color:var(--blue)}
.expertise .section-title{position:absolute;left:176px;top:184px;font-size:52px;line-height:58px}
.service{position:absolute;width:245px}
.service h3{font-size:15px;font-weight:800;color:var(--blue);letter-spacing:.3px;margin-bottom:14px;white-space:nowrap}
.service p{font-size:13.5px;line-height:23px;color:var(--ink)}

.who{top:1419px;height:528px}
.who-photo{position:absolute;inset:0;background:linear-gradient(120deg,#7fabd3 0%,var(--photo) 50%,#a8c8e4 100%)}
.who .section-title{position:absolute;top:55px;width:100%;text-align:center;font-size:50px;color:var(--white)}
.who-copy{position:absolute;left:129px;top:156px;width:940px;color:var(--white);font-size:13.5px;line-height:23px}
.who-copy p{margin-bottom:23px}

.approach{top:1947px;height:525px}
.approach-panel{position:absolute;left:705px;top:0;width:495px;height:525px;background:var(--mist)}
.approach .section-title{position:absolute;left:823px;top:200px;font-size:52px;line-height:58px}
.approach-copy{position:absolute;left:86px;top:62px;width:525px;color:var(--blue-deep);font-size:13.5px;line-height:23px}
.approach-copy p{margin-bottom:23px}

.clients{top:2472px;height:353px;background:var(--teal-soft)}
.clients .section-title{position:absolute;top:52px;width:100%;text-align:center;font-size:52px;color:var(--white)}
.client{position:absolute;width:160px;margin-left:-80px;text-align:center;color:var(--white);font-weight:700;font-size:20px;display:flex;align-items:center;justify-content:center;gap:8px;white-space:nowrap}
.client i{display:inline-block;width:14px;height:14px;border-radius:50%;background:var(--white)}

.news{top:2825px;height:424px}
.news .section-title{position:absolute;top:50px;width:100%;text-align:center;font-size:52px;color:var(--blue)}
.post{position:absolute;top:150px;width:330px}
.post h3{font-size:17px;line-height:22px;font-weight:700;color:var(--sky)}
.post-meta{margin-top:15px;font-size:12.5px;color:var(--grey)}
.post-meta span{margin-left:22px}
.post p{margin-top:12px;font-size:13.5px;line-height:23px;color:var(--ink)}
.post a{display:inline-block;margin:4px 0 0 5px;font-size:15px;color:var(--ink);text-decoration:none;border-bottom:3px solid var(--teal)}

.newsletter{top:3249px;height:234px;background:var(--news-sub);text-align:center;color:var(--white)}
.newsletter h2{position:absolute;top:42px;width:100%;font-family:var(--serif);font-weight:400;font-size:36px}
.newsletter p{position:absolute;top:93px;width:100%;font-family:var(--serif);font-size:26px;color:#e3eef8}
.signup-input{position:absolute;left:380px;top:149px;width:342px;height:35px;background:var(--white);border-radius:3px;text-align:left;padding:9px 10px;font-size:13px;color:#c9d3dc}
.signup-btn{position:absolute;left:732px;top:149px;width:88px;height:35px;background:var(--blue);border-radius:3px;font-size:14px;line-height:35px;color:var(--white)}

.build{top:3483px;height:417px;background:var(--build)}
.build h2{position:absolute;top:60px;width:100%;text-align:center;font-family:var(--serif);font-weight:400;font-size:36px;color:var(--build-title);letter-spacing:.5px}
</style>
</head>
<body>

<header class="site-header">
  <div class="brand">Holvencrest Ventures</div>
  <nav class="nav">
    <a style="left:843px">HOME</a>
    <a style="left:932px">ABOUT US</a>
    <a style="left:1049px">CONTACT</a>
  </nav>
</header>

<section class="hero">
  <div class="hero-photo" role="img" aria-label="City skyline with construction cranes under a blue tint"></div>
  <p class="hero-kicker">Holvencrest Ventures is a venture capital studio firm</p>
  <h1 class="hero-title">Raising solid capital for startups and<br>helping businesses jumpstart their revenue</h1>
  <svg class="hero-arrow" width="30" height="20" viewBox="0 0 30 20"><polyline points="3,4 15,16 27,4" fill="none" stroke="#fff" stroke-width="4" stroke-linecap="round" stroke-linejoin="round"/></svg>
</section>

<section class="stats">
  <div class="stat" style="left:73px"><div class="stat-value">$40M+</div><div class="stat-label">MONEY RAISED</div></div>
  <div class="stat" style="left:339px"><div class="stat-value">$125M+</div><div class="stat-label">ATTRIBUTED REVENUE</div></div>
  <div class="stat" style="left:604px"><div class="stat-value">11</div><div class="stat-label">COMPANY EXITS</div></div>
  <div class="stat" style="left:858px"><div class="stat-value">2</div><div class="stat-label">AWARDS WON</div></div>
</section>

<section class="expertise">
  <div class="expertise-panel"></div>
  <h2 class="section-title">Area of<br>Expertise</h2>
  <div class="service" style="left:589px;top:55px"><h3>NETWORK SUPPORT</h3><p>Help you build your network, intro-<br>ducing you to the right people in the<br>right places.</p></div>
  <div class="service" style="left:881px;top:55px"><h3>REVENUE ACCELERATION</h3><p>Analyze your revenue streams, pro-<br>viding solutions for kickstarting your<br>revenue</p></div>
  <div class="service" style="left:589px;top:220px"><h3>MERGERS &amp; ACQUSITIONS</h3><p>Facilitate a smooth mergers and ac-<br>quisition process for the expansion of<br>your business</p></div>
  <div class="service" style="left:879px;top:220px"><h3>INTEGRATION &amp; INCUBATION</h3><p>Providing training and guidance for<br>startups looking to make their mark<br>on the world.</p></div>
  <div class="service" style="left:589px;top:379px"><h3 style="margin-left:7px">RAISING CAPITAL</h3><p>Reach out to our extensive connec-<br>tions to raise vital capital for your<br>startup.</p></div>
  <div class="service" style="left:881px;top:379px"><h3 style="margin-left:2px">MARKETING</h3><p>Consult on marketing process,<br>strategies and implementation<br>across your startup.</p></div>
</section>

<section class="who">
  <div class="who-photo" role="img" aria-label="Hands working at a laptop and paperwork under a pale blue tint"></div>
  <h2 class="section-title">Who We Are</h2>
  <div class="who-copy">
    <p>Holvencrest Ventures is a venture capital studio firm based in Austin TX with a laser focus on raising solid capital for startups and helping businesses jumpstart their revenue.</p>
    <p>Founded in 2020 by investment expert Marcus Holven, Holvencrest Ventures combines proven experience in the venture capital field with a data-driven business analysis strategy to secure capital and reinforce revenue streams for startups and established businesses. Born from the idea that the best way to help founders thrive is to understand their strengths, their weaknesses, their ambitions and their needs - our specialists have been through the entire startup process themselves, and that experience forms our unique approach to business support.</p>
    <p>Marcus's work in the sector has seen him take on the biggest and the best, working with iconic business figures to leave an indelible mark on the U.S. startup scene. He brings all of that expertise to the table at Holvencrest Ventures, leading a dedicated team to support the finest international businesses to reach, break through and go beyond their potential.</p>
  </div>
</section>

<section class="approach">
  <div class="approach-panel"></div>
  <h2 class="section-title">Our<br>Approach</h2>
  <div class="approach-copy">
    <p>We've built our approach to helping your startup thrive based around three key developmental pillars that guarantee results for our partners.</p>
    <p>First pillar is expertise. We've built our firm on a bank of insights, knowledge and proficiencies honed over years of working with the biggest names in venture capitalism – that experience forms the backbone of every project, every pitch and every investment.</p>
    <p>Second pillar is collaboration. We believe that the best partnerships start with a combined and cooperative approach that benefits all parties every step of the way. We'll always keep our partners up-to-date with our work using regular touchpoints and reports.</p>
    <p>Third and final pillar is trust. We know that our clients and our partners know their industry better than we do, so we trust their input and their ideas – pairing them up with our own business intelligence to guarantee success.</p>
  </div>
</section>

<section class="clients">
  <h2 class="section-title">Our Clients</h2>
  <div class="client" style="left:144px;top:160px"><i></i>Quarvelle</div>
  <div class="client" style="left:287px;top:160px">Lintorra</div>
  <div class="client" style="left:449px;top:160px"><i></i>Brevanox</div>
  <div class="client" style="left:599px;top:160px">Oplathe</div>
  <div class="client" style="left:775px;top:160px"><i></i>Tavriquo</div>
  <div class="client" style="left:914px;top:160px">Nuvessa</div>
  <div class="client" style="left:1052px;top:160px">Farrowen</div>
  <div class="client" style="left:151px;top:245px"><i></i>Keltrova</div>
  <div class="client" style="left:291px;top:245px">Dovarin</div>
  <div class="client" style="left:456px;top:245px">Pellwick</div>
  <div class="client" style="left:616px;top:245px"><i></i>Corvanth</div>
  <div class="client" style="left:772px;top:245px">Zenthari</div>
  <div class="client" style="left:911px;top:245px">Wayloria</div>
  <div class="client" style="left:1052px;top:245px">Homarvel</div>
</section>

<section class="news">
  <h2 class="section-title">Latest News</h2>
  <article class="post" style="left:85px">
    <h3>We've built our firm on a bank of insights, knowledge and proficiencies</h3>
    <div class="post-meta">10.12.2021<span>Auther Name</span></div>
    <p>Aenean imperdiet. Etiam ultricies nisi vel augue. Curabitur ullamcorper ultricies nisi. Nam eget dui. Etiam rhoncus. Maecenas tempus, tellus eget condimentum rhoncus, sem quam semper libero,</p>
    <a>Read more</a>
  </article>
  <article class="post" style="left:439px">
    <h3>We believe that the best partnerships start with a combined and cooperative</h3>
    <div class="post-meta">10.12.2021<span>Auther Name</span></div>
    <p>Aenean imperdiet. Etiam ultricies nisi vel augue. Curabitur ullamcorper ultricies nisi. Nam eget dui. Etiam rhoncus. Maecenas tempus, tellus eget condimentum rhoncus, sem quam semper libero,</p>
    <a>Read more</a>
  </article>
  <article class="post" style="left:788px">
    <h3>We know that our clients and our partners know their industry better</h3>
    <div class="post-meta">10.12.2021<span>Auther Name</span></div>
    <p>Aenean imperdiet. Etiam ultricies nisi vel augue. Curabitur ullamcorper ultricies nisi. Nam eget dui. Etiam rhoncus. Maecenas tempus, tellus eget condimentum rhoncus, sem quam semper libero,</p>
    <a>Read more</a>
  </article>
</section>

<section class="newsletter">
  <h2>Want to get up to date news?</h2>
  <p>Subscribe to Our Newsletter</p>
  <div class="signup-input">Your email</div>
  <div class="signup-btn">SIGN UP</div>
</section>

<section class="build">
  <h2>BUILD WITH US</h2>
</section>

</body>
</html>
```